Dynamic Templates

Our company hosts web stores for our clients. They can set up as many as they wish on our platform, and select from the stock templates we provide. We are looking to increase the number of available stock templates.

Because our users can dynamically control many of the template elements - specifically colors - they have to be flexible and abide by certain rules. These rules are spelled out in the attached documents.

Here are links to two of our most used templates:
http://fernridge.vexalcart.example/
http://stampled.vexalcart.example/

Templates need to have a landing page (what you see when first clicking one of the above links). There also needs to be a category page (what you see when clicking any category) and a product detail page (what you see when you arrive at an individual product, where there are various cart options like Buy Now or Request Info).

```html
<!DOCTYPE html>
<html lang="en">
<head>
<meta charset="utf-8">
<title>VexalMerch – Promotional Products</title>
<link href="https://fonts.googleapis.com/css2?family=Fira+Sans:wght@400;500;600&display=swap" rel="stylesheet">
<style>
:root{
  --plum-deep:#2c0634;
  --plum:#4a0c55;
  --plum-glow:#8a2a8e;
  --magenta:#9b3a98;
  --accent:#f39a2a;
  --ink:#222222;
  --heading:#5a1a62;
  --headline:#3a1043;
  --panel:#f0f0f0;
  --white:#ffffff;
  --rule:#7a4c82;
}
*{margin:0;padding:0;box-sizing:border-box}
html,body{width:1200px;height:974px;overflow:hidden}
body{
  position:relative;
  font-family:"Fira Sans","Trebuchet MS",sans-serif;
  color:var(--ink);
  background:linear-gradient(#dcdcdc 281px,#ececec 420px,#ffffff 560px);
}
.masthead{
  position:absolute;left:0;top:0;width:1200px;height:281px;
  background:
    radial-gradient(ellipse 520px 90px at 640px 120px,rgba(232,170,235,.75),rgba(160,60,170,.35) 50%,transparent 80%),
    radial-gradient(ellipse 700px 200px at 200px 0,rgba(120,20,130,.8),transparent 70%),
    linear-gradient(var(--plum) 0,var(--plum-deep) 100%);
}
.brand{position:absolute;left:75px;top:52px;display:flex;align-items:center;gap:10px}
.brand-dot{width:42px;height:42px;border-radius:50%;background:var(--accent)}
.brand-name{font-size:20px;font-weight:500;color:var(--white)}
.top-contact{position:absolute;right:88px;top:64px;font-size:13px;font-weight:600;color:var(--white)}
.frame{
  position:absolute;left:75px;top:141px;width:1046px;height:300px;
  background:var(--white);border-radius:8px 8px 0 0;
}
.hero{
  position:absolute;left:19px;top:14px;width:991px;height:278px;
  border-radius:6px;overflow:hidden;
  background:linear-gradient(90deg,#dcdcdc 0,#f6f6f6 35%,#ffffff 70%);
  box-shadow:inset 0 0 0 1px #e2e2e2;
}
.hero-decor{position:absolute;left:0;top:0;width:560px;height:278px;background:radial-gradient(ellipse 300px 140px at 280px 150px,rgba(200,210,210,.35),transparent 75%)}
.hero-photo{
  position:absolute;right:2px;top:6px;width:434px;height:280px;
  background:linear-gradient(160deg,#f4e6d8 0%,#e8b9b0 45%,#d84a3a 75%,#f07a3a 100%);
  border-radius:4px 0 0 0;
}
.hero-copy{position:absolute;left:26px;top:100px;color:var(--headline)}
.hero-copy h1{font-size:26px;font-weight:400;line-height:32px}
.hero-copy p{font-size:22px;line-height:28px}
.btn-shop{
  position:absolute;left:26px;top:217px;width:152px;height:34px;
  display:flex;align-items:center;justify-content:center;gap:5px;
  background:linear-gradient(#8e2a8a,#5e0f5c);border-radius:4px;
  color:var(--white);font-size:15px;font-weight:600;
}
.intro{position:absolute;left:75px;top:440px;width:1046px;height:294px;background:var(--panel);padding:34px 25px 0 25px}
.intro h2{font-size:19.5px;font-weight:500;color:var(--heading);margin-bottom:16px}
.intro h3{font-size:15px;font-weight:600;color:var(--heading);margin:16px 0 16px}
.intro p{font-size:14px;line-height:17px;margin-bottom:16px}
.footer{
  position:absolute;left:75px;top:734px;width:1046px;height:240px;
  background:radial-gradient(ellipse 500px 120px at 300px 20px,rgba(140,40,140,.55),transparent 75%),var(--plum-deep);
  color:var(--white);
}
.box{position:absolute;top:26px;height:184px;border:1px solid var(--rule)}
.box-title{position:absolute;top:-14px;left:14px;padding:0 4px;background:transparent;font-size:19px;font-weight:500;display:flex;align-items:center;gap:4px;line-height:24px}
.box-title::before{content:"";position:absolute;left:0;right:0;top:12px;height:2px;background:var(--plum-deep);z-index:-1}
.box ul{list-style:none;font-size:13px;line-height:19.6px}
.cat-box{left:26px;width:543px}
.cat-cols{position:absolute;left:16px;top:20px;display:flex;gap:0}
.cat-cols ul{width:196px}
.price-box{left:594px;width:171px}
.price-box ul{position:absolute;left:18px;top:20px}
.search-box{left:787px;width:229px}
.search-row{position:absolute;left:11px;top:23px;display:flex;gap:6px}
.search-row span{display:block;width:176px;height:26px;background:var(--white);border:1px solid #bbb}
.search-go{width:27px;height:26px;background:var(--magenta);font-size:11px;display:flex;align-items:center;justify-content:center}
.contact-title{position:absolute;left:11px;top:63px;font-size:19px;font-weight:500;display:flex;align-items:center;gap:4px}
.contact-lines{position:absolute;left:11px;top:95px;font-size:13px;font-weight:500;line-height:15.5px}
</style>
</head>
<body>
<header class="masthead">
  <div class="brand"><span class="brand-dot"></span><span class="brand-name">VexalMerch</span></div>
  <div class="top-contact">Demo User . (415) 555-0142 . info@vexalcart.example</div>
</header>

<section class="frame">
  <div class="hero">
    <div class="hero-decor" role="img" aria-label="Faint butterfly silhouettes in the background"></div>
    <div class="hero-photo" role="img" aria-label="Smiling shopper holding colourful shopping bags"></div>
    <div class="hero-copy">
      <h1>You will find a lot of brand new products for<br>the cheapest price in the market.</h1>
      <p>Start your fun shopping now!</p>
      <span class="btn-shop">
        <svg width="16" height="14" viewBox="0 0 16 14" aria-hidden="true"><path d="M0 1h3l2 8h8l2-6H4" fill="none" stroke="#fff" stroke-width="1.8"/><circle cx="6" cy="12" r="1.4" fill="#fff"/><circle cx="12" cy="12" r="1.4" fill="#fff"/></svg>
        Start Shopping
      </span>
    </div>
  </div>
</section>

<main class="intro">
  <h2>Welcome To The Future of Promotional Products!</h2>
  <p>Gone are the days of searching through dog-eared catalogs or trying to make sense of complicated product websites.</p>
  <p>We do the work for you! We've taken only the very best and most current products and placed them in easy-to-use categories designed for your needs.<br>Take a look at our selection - quality products at excellent prices.</p>
  <h3>Enjoy This Amazing New Resource</h3>
  <p>We know you don't have time to waste; so we've cut to the chase and made it simple! But keep in mind, we do have access to over a million products - so if you don't see what you're looking for or have a special theme or request, let us know - we'll find it!</p>
</main>

<footer class="footer">
  <div class="box cat-box">
    <div class="box-title">» Shop By Category</div>
    <div class="cat-cols">
      <ul><li>Apparel</li><li>Business Supplies</li><li>Company Outings</li><li>Eco Friendly</li><li>Food, Candy &amp; Drink</li><li>Golf, Sports &amp; Outdoors</li><li>Mugs &amp; Drinkware</li><li>Tradeshows &amp; Events</li></ul>
      <ul><li>Awards &amp; Recognition</li><li>Caps &amp; Hats</li><li>Corporate Gifts</li><li>Electronics</li><li>Games &amp; Novelties</li><li>Healthcare &amp; Safety</li><li>Notebooks &amp; Folios</li><li>Writing Instruments</li></ul>
      <ul><li>Bags &amp; Totes</li><li>Clocks &amp; Watches</li><li>Desktop &amp; Office</li><li>Executive Gifts</li><li>Gift Sets</li><li>Keychains</li><li>Tools &amp; Hardware</li></ul>
    </div>
  </div>
  <div class="box price-box">
    <div class="box-title">»Shop By Price</div>
    <ul><li>Under $5</li><li>$5 - $10</li><li>$10 - $20</li><li>$20 - $50</li><li>$50 - $100</li><li>$100 - $200</li><li>Over $200</li></ul>
  </div>
  <div class="box search-box">
    <div class="box-title">
      <svg width="15" height="15" viewBox="0 0 15 15" aria-hidden="true"><circle cx="6" cy="6" r="4.2" fill="none" stroke="#fff" stroke-width="2"/><path d="M9 9l5 5" stroke="#fff" stroke-width="2.4"/></svg>Quick Search
    </div>
    <div class="search-row"><span></span><div class="search-go">GO</div></div>
    <div class="contact-title">
      <svg width="13" height="20" viewBox="0 0 13 20" aria-hidden="true"><rect x="1" y="1" width="11" height="18" rx="1.5" fill="none" stroke="#fff" stroke-width="1.6"/><rect x="3" y="3.5" width="7" height="6" fill="#fff"/><circle cx="6.5" cy="15" r="1.3" fill="#fff"/></svg>Contact Us
    </div>
    <div class="contact-lines">Tel: 345 555 0134<br>Fax: 345 555 0135<br>EMail: info@vexalcart.example<br>www.vexalcart.example</div>
  </div>
</footer>
</body>
</html>
```